Website - Corla Druvick

I need a website that has multiple pages and easy for me to update pictures, content and blogs as an ongoing basis’s.
It will have videos and needs to be compatible to view easily and aesthetically on mobile phones.
Please refer to this website for inspiration www.lorettaquisp.com

Coding

Coded - Design and coding required

Number of Pages Required

5+ page

Font styles to use
Other font styles liked:
• Refer to website provided as inspiration

Requirements
Must have
• Please use stock images for now to do design, but I will be providing all imagery, videos and content

```html
<!DOCTYPE html>
<html lang="en">
<head>
<meta charset="utf-8">
<title>Corla Druvick</title>
<link rel="stylesheet" href="https://fonts.googleapis.com/css2?family=Yellowtail&family=Didact+Gothic&display=swap">
<style>
:root{
  --ink:#111;
  --white:#fff;
  --paper:#f7f7f7;
  --muted:#bdbdbd;
  --text:#222;
}
*{box-sizing:border-box;margin:0;padding:0}
html,body{width:1200px;height:3459px;overflow:hidden}
body{position:relative;background:var(--white);font-family:"Didact Gothic",sans-serif;color:var(--text)}
.abs{position:absolute}
.script{font-family:"Yellowtail",cursive;color:var(--ink);font-weight:400}
.photo{position:absolute}
.logo{left:172px;top:26px;font-size:38px}
.nav{position:absolute;top:38px;left:663px;display:flex;gap:0;font-size:17px;color:var(--ink)}
.nav a{position:absolute;white-space:nowrap;color:var(--ink);text-decoration:none}
.hero-left{left:88px;top:100px;width:355px;height:594px;background:linear-gradient(160deg,#fafafa 0%,#cfcfcf 40%,#3a3a3a 70%,#d8d8d8 100%)}
.hero-right{left:592px;top:0;width:608px;height:600px;background:linear-gradient(135deg,#f2f2f2 0%,#cdcdcd 40%,#5a5a5a 60%,#dcdcdc 100%)}
.hero-gown{left:172px;top:694px;width:327px;height:435px;background:radial-gradient(ellipse at 55% 70%,#b79ad8 0%,#6c4f8d 35%,#0a0a0a 75%)}
.stem{left:937px;top:600px;width:2px;height:72px;background:var(--ink)}
.stem-dot{left:932px;top:668px;width:12px;height:12px;border-radius:50%;background:var(--ink)}
.about-title{right:173px;top:718px;font-size:48px;text-align:right}
.about-text{left:537px;top:796px;width:490px;font-size:14.5px;line-height:28.5px;text-align:right;text-align-last:right}
.btn{position:absolute;background:var(--ink);color:var(--white);font-size:13.5px;display:flex;align-items:center;justify-content:center;letter-spacing:.2px}
.about-btn{left:917px;top:1023px;width:108px;height:51px}
.band-grey{position:absolute;left:0;width:1200px;background:var(--paper)}
.blog-band{top:1129px;height:788px}
.section-title{position:absolute;left:0;width:1200px;text-align:center;font-size:46px}
.blog-title{top:1210px}
.blog-photo{left:172px;top:1319px;width:307px;height:447px;background:linear-gradient(180deg,#3c7fd4 0%,#6ea4de 35%,#2c5f86 50%,#d8c2a0 68%,#c9b08a 100%)}
.blog-card{position:absolute;left:456px;top:1381px;width:571px;height:421px;background:var(--white);box-shadow:0 4px 14px rgba(0,0,0,.16)}
.blog-card h3{position:absolute;left:31px;top:42px;font-size:21px;font-weight:400;color:var(--ink)}
.date{position:absolute;left:31px;top:91px;width:91px;height:35px;background:var(--muted);color:var(--white);font-size:11.5px;display:flex;align-items:center;justify-content:center}
.blog-card p{position:absolute;left:31px;width:516px;font-size:12.5px;line-height:22.5px;text-align:justify}
.blog-card .p1{top:147px}
.blog-card .p2{top:229px}
.blog-btn{left:31px;top:324px;width:109px;height:49px}
.arrow{position:absolute;top:1507px}
.video-title{top:1990px}
.video{position:absolute;top:2094px;width:271px;height:338px}
.play{position:absolute;left:50%;top:50%;width:56px;height:56px;transform:translate(-50%,-50%)}
.load-btn{left:546px;top:2486px;width:108px;height:51px}
.social-band{top:2620px;height:449px}
.insta-title{top:2681px}
.insta{position:absolute;top:2787px;width:226px;height:202px}
.footer{position:absolute;left:0;top:3069px;width:1200px;height:390px;background:#000}
.footer-logo{position:absolute;left:0;width:1200px;top:3144px;text-align:center;font-size:40px;color:var(--white)}
.social{position:absolute;top:3251px;width:42px;height:42px;border-radius:50%;background:var(--white);color:var(--ink);font-size:10px;display:flex;align-items:center;justify-content:center}
.footer-rule{position:absolute;left:172px;top:3359px;width:855px;height:1px;background:var(--white)}
.copyright{position:absolute;left:0;width:1200px;top:3398px;text-align:center;font-size:15px;color:var(--white)}
</style>
</head>
<body>

<header>
  <div class="abs script logo">Corla Druvick</div>
  <nav class="nav">
    <a style="left:0">Home</a>
    <a style="left:77px">About</a>
    <a style="left:156px">Blog</a>
    <a style="left:221px">Stories</a>
    <a style="left:306px">Contact</a>
  </nav>
</header>

<section class="about">
  <div class="photo hero-left" role="img" aria-label="Black and white portrait of the model in a strapless bodysuit"></div>
  <div class="photo hero-right" role="img" aria-label="Black and white studio photo of the model posing on the floor in boots"></div>
  <div class="photo hero-gown" role="img" aria-label="Model in a lilac tulle gown on a starry stage backdrop"></div>
  <div class="abs stem"></div>
  <div class="abs stem-dot"></div>
  <h2 class="abs script about-title">About Corla Druvick</h2>
  <p class="abs about-text">Nam libero tempore, cum soluta nobis est eligendi optio cumque nihil im pedit quo minus id quod maxime placeat facere possimus, omnis voluptas assumenda est, omnis dolor repellendus. Temporibus autem quibusdam et aut officiis debitis aut rerum necessitatibus saepe eveniet ut et voluptates repudiandae sint et molestiae non recusandae. Itaque earum rerum hic te netur a sapiente delectus, ut aut reiciendis voluptatibus maiores alias con sequatur aut perferendis doloribus asperiores repellat</p>
  <a class="btn about-btn">READ MORE</a>
</section>

<section class="band-grey blog-band"></section>
<h2 class="section-title script blog-title">Our Blog Posts</h2>
<div class="photo blog-photo" role="img" aria-label="Model kneeling on a sunny beach in sportswear"></div>
<article class="blog-card">
  <h3>Miss Starlight Coastal National Finalist 2021</h3>
  <div class="date">Jan 20, 2021</div>
  <p class="p1">Nam libero tempore, cum soluta nobis est eligendi optio cumque nihil impedit quo minus id quod maxime placeat facere possimus, omnis voluptas assumenda est, omnis dolor repellendu. temporibus autem quibusdam.</p>
  <p class="p2">Cum soluta nobis est eligendi optio cumque nihil impedit quo minus id quod maxime placeat facere possimus, omnis voluptas assumenda est, omnis dolor repellendu. tempori-bus autem quibusdam.</p>
  <a class="btn blog-btn">READ MORE</a>
</article>
<svg class="arrow" style="left:78px" width="26" height="72" viewBox="0 0 26 72"><polyline points="24,1 2,36 24,71" fill="none" stroke="#111" stroke-width="2"/></svg>
<svg class="arrow" style="left:1105px" width="26" height="72" viewBox="0 0 26 72"><polyline points="2,1 24,36 2,71" fill="none" stroke="#111" stroke-width="2"/></svg>

<section class="videos">
  <h2 class="section-title script video-title">Our Videos</h2>
  <div class="video" style="left:-121px;background:linear-gradient(180deg,#9bb3c8 0%,#b89a86 45%,#3c3a38 100%)" role="img" aria-label="Video still of friends posing in a street">
    <svg class="play" style="left:221px" viewBox="0 0 56 56"><circle cx="28" cy="28" r="26" fill="none" stroke="#fff" stroke-width="3"/><polygon points="21,16 41,28 21,40" fill="none" stroke="#fff" stroke-width="3" stroke-linejoin="round"/></svg>
  </div>
  <div class="video" style="left:172px;background:linear-gradient(180deg,#101a4a 0%,#1e2a6a 40%,#1c8a6e 70%,#0d2a3a 100%)" role="img" aria-label="Video still of a pageant winner with sash and bouquet">
    <svg class="play" viewBox="0 0 56 56"><circle cx="28" cy="28" r="26" fill="none" stroke="#fff" stroke-width="3"/><polygon points="21,16 41,28 21,40" fill="none" stroke="#fff" stroke-width="3" stroke-linejoin="round"/></svg>
  </div>
  <div class="video" style="left:464px;background:linear-gradient(180deg,#2a2620 0%,#8c7a58 45%,#c8a878 65%,#2a2420 100%)" role="img" aria-label="Video still of three performers in gold sequin costumes">
    <svg class="play" viewBox="0 0 56 56"><circle cx="28" cy="28" r="26" fill="none" stroke="#fff" stroke-width="3"/><polygon points="21,16 41,28 21,40" fill="none" stroke="#fff" stroke-width="3" stroke-linejoin="round"/></svg>
  </div>
  <div class="video" style="left:757px;background:linear-gradient(180deg,#7ea0c6 0%,#d8c0a8 40%,#5d6f86 60%,#3a3028 100%)" role="img" aria-label="Video still of the model on a ship deck at sunset">
    <svg class="play" viewBox="0 0 56 56"><circle cx="28" cy="28" r="26" fill="none" stroke="#fff" stroke-width="3"/><polygon points="21,16 41,28 21,40" fill="none" stroke="#fff" stroke-width="3" stroke-linejoin="round"/></svg>
  </div>
  <div class="video" style="left:1048px;background:linear-gradient(180deg,#9cc2e2 0%,#4c6a4a 35%,#e58ab8 60%,#6b5a4a 100%)" role="img" aria-label="Video still of the model in a pink dress on a jetty">
    <svg class="play" style="left:135px" viewBox="0 0 56 56"><circle cx="28" cy="28" r="26" fill="none" stroke="#fff" stroke-width="3"/><polygon points="21,16 41,28 21,40" fill="none" stroke="#fff" stroke-width="3" stroke-linejoin="round"/></svg>
  </div>
  <a class="btn load-btn">LOAD MORE</a>
</section>

<section class="band-grey social-band"></section>
<h2 class="section-title script insta-title">@Snapline</h2>
<div class="insta" style="left:12px;background:linear-gradient(135deg,#e8e4de 0%,#8a5a3c 45%,#f0ebe4 100%)" role="img" aria-label="Snapline post: smiling portrait in a white top"></div>
<div class="insta" style="left:250px;background:linear-gradient(135deg,#d8d6d2 0%,#f07a1e 45%,#1e1e24 100%)" role="img" aria-label="Snapline post: the model in an orange knit with a mug"></div>
<div class="insta" style="left:487px;background:linear-gradient(135deg,#8cc0c4 0%,#7a5a44 45%,#f2eee8 100%)" role="img" aria-label="Snapline post: mirror selfie with a phone"></div>
<div class="insta" style="left:725px;background:linear-gradient(135deg,#e6e8ea 0%,#2aa0a6 50%,#cfd2d4 100%)" role="img" aria-label="Snapline post: the model in a teal dress by a doorway"></div>
<div class="insta" style="left:962px;background:linear-gradient(135deg,#7ab8cc 0%,#8a5a3c 45%,#e88870 100%)" role="img" aria-label="Snapline post: the model holding a smoothie"></div>

<footer class="footer"></footer>
<div class="script footer-logo">Corla Druvick</div>
<div class="social" style="left:441px">Pulse</div>
<div class="social" style="left:510px">Chirp</div>
<div class="social" style="left:579px">Scroll</div>
<div class="social" style="left:647px">Reel</div>
<div class="social" style="left:716px">Feed</div>
<div class="footer-rule"></div>
<p class="copyright">Copyrights @ 2021 Corla Druvick. All Rights Reserved.</p>

</body>
</html>
```